Halvorn Analytics, Inc. Site Design Project

Halvorn Analytics, Inc is my private and small research office.
This naming shows:
We investigate every(*: asterisk) issue to support society.
We investigate "a star risk" which means every critical things for example, information security, branding, public communication - to understand for our clients - especially innovative person.
Last year, we had faced the great disaster in Japan, we investigated the damaged place, schools, and local governments, and supported communities like PLUMvaskel.
So I want to get a high concept sites with good logo and to use card, website, and our letter.
Reason: We would like to look for more competitive candidates.
I uploaded the latest logo. If you have any idea to adapt it to your design, I appreciate it.
Target Market(s)
* marketing section of leading companies(enterprises)
* promotion agencies of government
* futurist and researcher
* business managers
Industry/Entity Type
Communication
Logo Text
for desirable future
Look and feel
Each slider illustrates characteristics of the customer's brand and the style your logo design should communicate.

```html
<!DOCTYPE html>
<html lang="en">
<head>
<meta charset="utf-8">
<title>Halvorn Analytics, Inc.</title>
<link rel="stylesheet" href="https://fonts.googleapis.com/css2?family=Michroma&family=Comfortaa:wght@700&family=Gelasio:ital@1&family=Arimo&display=swap">
<style>
  :root {
    --bg-deep: #9e140d;
    --bg-glow: #f57a3c;
    --frame: #0b0b0b;
    --screen: #ebeae6;
    --ink: #111111;
    --accent: #d42a1c;
    --copy-orange: #f28a5a;
    --white: #ffffff;
    --muted: #d9d0cc;
    --footer-red: #ff0000;
    --footer-edge: #7a0c08;
  }
  * { margin: 0; padding: 0; box-sizing: border-box; }
  html, body { width: 1200px; height: 1078px; overflow: hidden; }
  body {
    position: relative;
    background:
      radial-gradient(ellipse 300px 230px at 600px 60px, var(--bg-glow) 0%, #e0502a 45%, rgba(180,30,18,0) 100%),
      linear-gradient(90deg, #8f1009 0%, var(--bg-deep) 12%, #b11a10 50%, var(--bg-deep) 88%, #8f1009 100%);
    font-family: "Arimo", Arial, sans-serif;
    color: var(--white);
  }
  .site-nav a {
    position: absolute;
    top: 169px;
    transform: translateX(-50%);
    font-family: "Michroma", sans-serif;
    font-size: 14px;
    color: var(--white);
    text-decoration: none;
    text-shadow: 0 1px 2px rgba(0,0,0,.45);
    white-space: nowrap;
  }
  .brand {
    position: absolute;
    left: 480px; top: 18px; width: 240px;
    text-align: center;
  }
  .brand-mark {
    display: block;
    width: 96px; height: 96px; margin: 0 auto 14px;
    border-radius: 50%;
    background: var(--accent);
  }
  .brand-name {
    font-family: "Michroma", sans-serif;
    font-size: 15px; line-height: 22px;
    color: var(--white);
  }
  .hero { position: absolute; left: 0; top: 0; }
  .hero-photo {
    position: absolute;
    left: 79px; top: 213px; width: 460px; height: 348px;
    background: linear-gradient(100deg, #6e3a22 0%, #b0775a 30%, #dcbfae 60%, var(--screen) 100%);
  }
  .hero-title {
    position: absolute;
    left: 552px; top: 352px;
    font-family: "Michroma", sans-serif;
    font-size: 30px; color: var(--ink);
    letter-spacing: -0.5px;
    white-space: nowrap;
  }
  .hero-sub {
    position: absolute;
    left: 552px; top: 397px;
    font-family: "Michroma", sans-serif;
    font-size: 16px; color: var(--accent);
    white-space: nowrap;
  }
  .section-title {
    position: absolute;
    font-family: "Comfortaa", sans-serif;
    font-weight: 700; font-size: 20px;
    color: var(--white);
    text-shadow: 1px 1px 0 #5a0a06, 0 0 3px rgba(0,0,0,.5);
  }
  .about-title { left: 103px; top: 668px; }
  .about-copy {
    position: absolute;
    left: 97px; top: 704px; width: 681px;
    font-size: 12.4px; line-height: 15.6px;
    color: var(--copy-orange);
    text-align: justify;
  }
  .testimonials-title { right: 90px; top: 668px; }
  .testimonial {
    position: absolute;
    left: 812px; top: 700px; width: 306px;
    font-family: "Gelasio", Georgia, serif;
    font-style: italic; font-size: 17.5px; line-height: 30px;
    color: var(--white);
    text-align: justify; text-align-last: right;
  }
  .testimonial-author {
    position: absolute;
    right: 89px; top: 855px;
    font-family: "Gelasio", Georgia, serif;
    font-style: italic; font-size: 18px;
    color: var(--accent);
  }
  .join-title { left: 107px; top: 887px; }
  .social { position: absolute; left: 104px; top: 924px; display: flex; gap: 19px; }
  .social a {
    display: block; width: 46px; height: 46px;
    border-radius: 8px;
    background: linear-gradient(180deg, #f0b08a 0%, #c2592f 100%);
    box-shadow: 0 14px 10px -10px rgba(255,255,255,.15);
  }
  .contact {
    position: absolute;
    right: 91px; top: 924px;
    text-align: right;
    font-size: 15px; line-height: 21px;
  }
  .contact-label { color: var(--accent); }
  .contact-value { color: var(--muted); }
  .site-footer {
    position: absolute;
    left: 55px; top: 1008px; width: 1098px; height: 80px;
    background: var(--footer-red);
    border: 4px solid var(--footer-edge);
    border-bottom: none;
    border-radius: 46px 46px 0 0;
  }
  .footer-nav {
    position: absolute; left: 0; right: 0; top: 20px;
    text-align: center; font-size: 14px;
  }
  .footer-nav a { color: var(--white); text-decoration: none; margin: 0 10px; }
  .footer-nav span { color: var(--white); }
  .copyright {
    position: absolute; left: 0; right: 0; top: 52px;
    text-align: center; font-size: 11px; color: #1a0000;
  }
</style>
</head>
<body>

<nav class="site-nav">
  <a href="#" style="left:154px">ABOUT US</a>
  <a href="#" style="left:289px">SERVICES</a>
  <a href="#" style="left:421px">CAREER</a>
  <a href="#" style="left:790px">QUERY</a>
  <a href="#" style="left:919px">FEEDBACK</a>
  <a href="#" style="left:1057px">CONTACT</a>
</nav>

<div class="brand">
  <span class="brand-mark"></span>
  <div class="brand-name">HALVORN<br>ANALYTICS, INC.</div>
</div>

<section class="hero">
  <svg width="1200" height="650" viewBox="0 0 1200 650" aria-hidden="true">
    <defs>
      <filter id="soft-shadow" x="-10%" y="-200%" width="120%" height="500%">
        <feGaussianBlur stdDeviation="10"/>
      </filter>
    </defs>
    <ellipse cx="607" cy="612" rx="500" ry="16" fill="#3a0503" opacity=".6" filter="url(#soft-shadow)"/>
    <path d="M93 200 H1122 Q1148 200 1148 226 V570 Q1148 584 1120 586 Q607 600 95 586 Q67 584 67 570 V226 Q67 200 93 200 Z" fill="var(--frame)"/>
    <rect x="79" y="213" width="1057" height="348" fill="var(--screen)"/>
    <circle cx="574" cy="584" r="9.5" fill="#7a1410"/>
    <circle cx="609" cy="584" r="9.5" fill="#a0a0a0"/>
    <circle cx="645" cy="584" r="9.5" fill="#a0a0a0"/>
  </svg>
  <div class="hero-photo" role="img" aria-label="Photo of a customer service agent wearing a headset and talking on a phone"></div>
  <div class="hero-title">Leadership experience</div>
  <div class="hero-sub">in customer interaction management</div>
</section>

<h2 class="section-title about-title">Little About Hello</h2>
<p class="about-copy">We investigate "a star risk" which means every critical things for example, information security, branding, public communication - to understand for our clients - especially innovative person. Last year, we had faced the great disaster in Japan, we investigated the damaged place, schools, and local governments, and supported communities like PLUMvaskel. We investigate "a star risk" which means every critical things for example, information security, branding, public communication - to understand for our clients - especially innovative person. Last year, we had faced the great disaster in Japan, we investigated the damaged place, schools, and local governments, and supported communities like PLUMvaskel.</p>

<h2 class="section-title testimonials-title">Testimonials</h2>
<p class="testimonial">Lorem ipsum dolor sit amet, consecte-tur adipiscing elit. Aliquam ut mauris sem, id egestas quam. In elementum fringilla molestie. Curabitur nisl nibh, pulvinar eget</p>
<p class="testimonial-author">Mira Castell</p>

<h2 class="section-title join-title">Join us</h2>
<div class="social">
  <a href="#" aria-label="Social network one"></a>
  <a href="#" aria-label="Social network two"></a>
  <a href="#" aria-label="Blog"></a>
</div>

<div class="contact">
  <div><span class="contact-label">Call us : </span><span class="contact-value">+91 - 5550142087</span></div>
  <div><span class="contact-label">Email us : </span><span class="contact-value">info@halvorn.com</span></div>
</div>

<footer class="site-footer">
  <div class="footer-nav">
    <a href="#">About Us</a><span>|</span>
    <a href="#">Services</a><span>|</span>
    <a href="#">Query</a><span>|</span>
    <a href="#">Feedback</a><span>|</span>
    <a href="#">Contact</a>
  </div>
  <div class="copyright">© 2012, All Rights Reserved</div>
</footer>

</body>
</html>
```